I need a business card design for a new dance business. I offer classical Indian dance tuition and also professional performances. I want to offer the community a variety of Indian dance experiences which include: group class and private tuition, school and preschool educational courses and workshops. dance theatre performances, community function workshops and performances, Kids Bollywood parties, wedding & conference performances, mouth percussion classes, Indian mythology/ dance costume and make up workshops.
The final design should communicate a feeling and impression of the vibrance and energy of Indian dance.
Updates
Hi Everyone,
Project Deadline Extended
Reason: I would like to refine a few changes to the details of this lovely design and we have run out of time!
Project Deadline Extended
Reason: Still waiting to hear back form designer re two possible changes to the card design. Tomorrow is the deadline and I have sent several messages but with no response. I need to see this through before selecting this lovely design.
Thank you.
Tara
Industry/Entity Type
Preschool
Requirements
Must have
- The front of the business card should have the photo of me (my face and torso), surrounded entirely by a border of bright magenta (to match the magenta of my lipstick - it is the same as the magenta on my skirt in the second photo). Within the top border I want (perhaps yellow-gold) writing to say "Tara Holloway - Artistic Director" and within the bottom border it should read "Silver Creek Kathak Studio." If you turn the card on its side the left border should have my telephone number: 0417 826 394 and the right-hand border should read: silvercreekkathakstudio@fernmail.example
The reverse of the card should be the orange of the dance costume
and I'd like the picture of my feet and legs to be on the right side of the back of the card as a side border. Centre-aligned on the orange background it should read (perhaps in dark magenta):
Indian dance classes + private tuition
School + preschool educational courses and workshops
Dance theatre performances
Community function workshops and performances
Children's Bollywood parties
Wedding + conference performances
Mouth percussion classes
Indian mythology and dance demonstration workshops
Dance costume and make-up workshops
Nice to have
- A lovely artistic but easy-to-read font would be nice.

```html
<!DOCTYPE html>
<html lang="en">
<head>
<meta charset="utf-8">
<title>Silver Creek Kathak Studio – Business Card</title>
<link rel="stylesheet" href="https://fonts.googleapis.com/css2?family=Montserrat:wght@700;800&display=swap">
<style>
  :root {
    --magenta: #c8197d;
    --magenta-deep: #a4125f;
    --gold: #f5e81c;
    --orange: #f49a1b;
    --orange-light: #f8b23f;
    --orange-deep: #e27d0c;
    --ink: #141414;
    --white: #ffffff;
    --pale: #eeeeee;
    --page: #ffffff;
  }
  * { box-sizing: border-box; margin: 0; padding: 0; }
  html, body {
    width: 1200px; height: 351px; overflow: hidden;
    background: var(--page);
    font-family: "Montserrat", Arial, sans-serif;
  }
  .canvas { position: relative; width: 1200px; height: 351px; }
  .card {
    position: absolute; top: 9px; width: 586px; height: 333px;
    border-radius: 14px; overflow: hidden;
  }

  /* Front */
  .card-front { left: 9px; background: linear-gradient(135deg, #fafafa 0%, var(--pale) 55%, #dcdcdc 100%); }
  .front-texture {
    position: absolute; left: 0; top: 52px; width: 100%; height: 232px;
    background: linear-gradient(160deg, #ffffff 0%, #ececec 45%, #f7f7f7 70%, #e2e2e2 100%);
  }
  .band {
    position: absolute; left: 0; width: 100%; background: var(--magenta);
    display: flex; align-items: center; white-space: nowrap; z-index: 2;
  }
  .band-top { top: 0; height: 52px; padding-left: 66px; gap: 18px; }
  .band-bottom { top: 284px; height: 49px; padding-left: 28px; }
  .name { color: var(--gold); font-weight: 800; font-size: 23px; letter-spacing: .2px; }
  .role { color: var(--gold); font-weight: 700; font-size: 13px; padding-top: 2px; }
  .studio-name { color: var(--gold); font-weight: 800; font-size: 20px; }
  .contact {
    position: absolute; left: 28px; top: 240px; z-index: 2;
    color: var(--ink); font-weight: 700; font-size: 11.5px; line-height: 20px;
    white-space: nowrap;
  }
  .portrait {
    position: absolute; left: 396px; top: 0; width: 190px; height: 333px;
    background: linear-gradient(180deg, #d94a2a 0%, #e9c2ac 25%, #f1a23a 55%, #e3891c 75%, var(--magenta-deep) 100%);
  }

  /* Back */
  .card-back { left: 605px; background: linear-gradient(135deg, var(--orange-light) 0%, var(--orange) 50%, var(--orange-deep) 100%); }
  .back-title-band {
    position: absolute; left: 0; top: 134px; width: 397px; height: 33px;
    background: var(--ink); display: flex; align-items: center; padding-left: 22px;
  }
  .back-title { color: var(--gold); font-weight: 800; font-size: 20px; white-space: nowrap; }
  .services {
    position: absolute; left: 20px; top: 182px;
    list-style: none; color: var(--white); white-space: nowrap;
    font-weight: 700; font-size: 9.8px; line-height: 15.3px; text-transform: uppercase;
  }
  .services li::before { content: "•"; margin-right: 8px; }
  .dancer-feet {
    position: absolute; left: 393px; top: 0; width: 193px; height: 333px;
    background: linear-gradient(180deg, #b91d6f 0%, #d0a23a 40%, #c8197d 60%, #e9b99a 85%, var(--magenta-deep) 100%);
  }
</style>
</head>
<body>
<div class="canvas">

  <section class="card card-front">
    <div class="front-texture" role="img" aria-label="Soft white geometric tile background"></div>
    <div class="portrait" role="img" aria-label="Photo of Tara in classical Indian dance costume and make-up, face and torso"></div>
    <div class="band band-top">
      <span class="name">TARA HOLLOWAY</span>
      <span class="role">(ARTISTIC DIRECTOR)</span>
    </div>
    <p class="contact">
      NUMBER: 0417 826 394<br>
      EMAIL: SILVERCREEKKATHAKSTUDIO@FERNMAIL.EXAMPLE
    </p>
    <div class="band band-bottom">
      <span class="studio-name">SILVER CREEK KATHAK STUDIO</span>
    </div>
  </section>

  <section class="card card-back">
    <div class="dancer-feet" role="img" aria-label="Photo of dancer's legs and feet in costume with ankle bells and painted soles"></div>
    <div class="back-title-band">
      <span class="back-title">SILVER CREEK KATHAK STUDIO</span>
    </div>
    <ul class="services">
      <li>Indian dance classes + private tuition</li>
      <li>School + preschool educational courses and workshops</li>
      <li>Dance theatre performances</li>
      <li>Community function workshops and performances</li>
      <li>Children's Bollywood parties</li>
      <li>Wedding + conference performances</li>
      <li>Mouth percussion classes</li>
      <li>Indian mythology and dance demonstration workshops</li>
      <li>Dance costume and make-up workshops</li>
    </ul>
  </section>

</div>
</body>
</html>
```